Democracy in crisis book

This book tries to sound the ALARM that we will lose our democracy unless we force Unionists to adopt the plan inside this book. I designed a mock cover (attached) but I am concerned it would not look good in the Thumbnail view that most people would see it as they're scrolling down Shopvale or Pagenook. The final title for the book is: Final Hour to Rescue the Free Republic. The current subtitle is: The Single Path to Halt the 2022 Partisan Takeover & Renew Our Homeland -- but it’s a work in progress.The subtitle is still working progress but it's really not that important and can be small.
STYLE CONSIDERATIONS:
(1) The title should be on 5 separate lines: Final; Hour; To Rescue; Free; Republic
(2) The title could be in white fat letters except for maybe one line that says “To Rescue” which could be in the blue color of the Civic Union Party-- or maybe Free Republic could be in blue. We may have to try a few variations of that.
(3) I picked the red in the mock cover to connotate an emergency,
(4) I liked big bold fat font going across the full page so that it looks like a major warning sign, though note I was unable to extend each line flush all the way to the right which I think would have been better.
(5) I liked it better flush to left instead of centered.
(6) I picked the Harwick monument + a crowd for my mock cover, but a picture of a huge crowd protesting with a picture of the United States Congress in the background would be much better. DO NOT USE HARWICK. Obviously I would need it to be an open license or something I can pay a small amount to get. If you can find that picture then the page should probably be colored in red with Congress in white.
I got the idea 4 giant title from the book “seldom a quiet so bright” and Dellowby’s “When Freedom Fades” or “Grey Herons” by Mara Vostell though I hate that font)
I love Osric Thale’s “marked since the outset” cover so if you find a picture of Congress and a protest crowd instead of painting it red you could have just a couple of jagged red stripes going across it like that cover.
I love the 3-D effect of Greta Wolven's cover for The Silverwren where it looks like a page is being ripped. That effect could be done the words Free Republic like it's being torn off the page UPDATE: MANY DESIGNERS TRIED THAT & IT DID NOT WORK AT ALL.
Note that this book will be submitted to many award competitions, so please give me an award-winning cover.
I like how the title of the book The Unchosen by Martin Fellowes has the words starting to fade. I don't like the ladder on it, but maybe 'Free Republic' could fade like that.
Unionists

```html
<!DOCTYPE html>
<html lang="en">
<head>
<meta charset="utf-8">
<title>Final Hour to Rescue the Free Republic — Cover</title>
<link href="https://fonts.googleapis.com/css2?family=Bebas+Neue&family=Oswald:wght@500&display=swap" rel="stylesheet">
<style>
  :root {
    --stage: #f2f2f2;
    --cover-red: #9c0b0b;
    --cover-red-bright: #b31212;
    --cover-red-deep: #3c0202;
    --title-white: #ffffff;
    --union-blue: #0d2a73;
  }
  html, body {
    margin: 0;
    width: 1200px;
    height: 1200px;
    overflow: hidden;
    background: var(--stage);
  }
  .cover {
    position: absolute;
    left: 236px;
    top: 40px;
    width: 728px;
    height: 1120px;
    overflow: hidden;
    background:
      radial-gradient(ellipse at 50% 70%, var(--cover-red-bright) 0%, var(--cover-red) 60%, #7d0808 100%);
  }
  .cover__artwork {
    position: absolute;
    left: 0;
    top: 0;
    width: 100%;
    height: 560px;
    background:
      radial-gradient(ellipse at 85% 45%, rgba(60, 2, 2, 0.55) 0%, rgba(60, 2, 2, 0) 45%),
      radial-gradient(ellipse at 25% 40%, rgba(60, 2, 2, 0.45) 0%, rgba(60, 2, 2, 0) 50%),
      linear-gradient(180deg, var(--cover-red-deep) 0%, #7a0606 35%, rgba(156, 11, 11, 0) 100%);
  }
  .title {
    margin: 0;
  }
  .title-line {
    position: absolute;
    left: 29px;
    margin: 0;
    font-family: "Bebas Neue", "Oswald", sans-serif;
    font-weight: 400;
    font-size: 190px;
    line-height: 1;
    letter-spacing: 1px;
    color: var(--title-white);
    white-space: nowrap;
  }
  .title-line--1 { top: 102px; }
  .title-line--2 { top: 282px; }
  .title-line--3 { top: 466px; color: var(--union-blue); }
  .title-line--4 { top: 642px; }
  .title-line--5 { top: 818px; }
  .subtitle {
    position: absolute;
    left: 406px;
    top: 130px;
    margin: 0;
    font-family: "Bebas Neue", "Oswald", sans-serif;
    font-size: 32px;
    line-height: 44px;
    color: var(--title-white);
    white-space: nowrap;
  }
  .author {
    position: absolute;
    left: 36px;
    top: 1004px;
    margin: 0;
    font-family: "Oswald", sans-serif;
    font-weight: 500;
    font-size: 36px;
    letter-spacing: 11px;
    color: var(--title-white);
    white-space: nowrap;
  }
</style>
</head>
<body>
  <main class="cover">
    <div class="cover__artwork" role="img" aria-label="Dark red storm clouds over a carved stone monument and a faint map, toned in deep red"></div>
    <h1 class="title">
      <span class="title-line title-line--1">Final;</span>
      <span class="title-line title-line--2">Hour;</span>
      <span class="title-line title-line--3">To Rescue;</span>
      <span class="title-line title-line--4">Free;</span>
      <span class="title-line title-line--5">Republic</span>
    </h1>
    <p class="subtitle">THE SINGLE PATH TO HALT<br>THE 2022 PARTISAN TAKEOVER<br>&amp; RENEW OUR HOMELAND</p>
    <p class="author">CORWIN BLAKE HALLORAN</p>
  </main>
</body>
</html>
```